Impack Proof Screen Protector Packaging Design Project

I want a sleek box design for an Impact Proof Screen Protection Shield" for mobile phones and tablet screens. Want to use this design for online website sale (eCommerce). Please use the colour combination which can effect customers physiology immediately.
Product Features:
Name: vela Guardwrap
Advanced Impact Protection Shield
Easy and Fast Application
Compatible With Stylus
Guaranteed Glue Free
Perfect Crystal Clear
Anti Fingerprint
No Air Bubble
Anti Bacterial
Anti scratch
Updates

come on guys...give me some best designs please

Project Deadline Extended
Reason: Have not received the best design yet...

Project Deadline Extended
Reason: still waiting for the best design

Project Deadline Extended

Project Deadline Extended

Project Deadline Extended

Hi,

Thanks for the design. I would like to make some changes.

I want main core colour black (HTML code of Black is 111C24)
Blue colour as aditional or second colour, (HTML code of BLUE is 0088CE)

AND another colour like Orange (HTML -> FF5800)  or Purple (HTML -> 9B1889) can be use as a ACCENT colour if needed.

Pure White, Silver and Greys like -> HTML codes -> 4D4F53 , D1D4D3 , AND C4D9E4 Can be use as support colours if needed.

please work on it and get back to me .

Thanks

Project Deadline Extended
Reason: work pending

Target Market(s)

UK & Europe is priority and then Global market

Industry/Entity Type

Online

Requirements
Must have
• All features must write with Pictures/thumbnail on back side.
Must have a hanger hook / hole.
Must have Recycling sign/logo on the edge.
Must have our website name "vela.co" on somewhere
its a sleek box design, size - This packing will be in 2 sizes:
a). 27cm X 11cm X 2cm
b). 25cm X 20cm X 2cm
Nice to have
• Impact Protection is main feature in this product, so can be highlighted with some weapon like sword or something like this...
Should not have
• Please try to not use a picture of any device like kelphone etc. because this packing will be use for number of different king of mobile phone/tablet devices.

```html
<!DOCTYPE html>
<html lang="en">
<head>
<meta charset="utf-8">
<title>vela Guardwrap – Packaging Front and Back</title>
<link rel="stylesheet" href="https://fonts.googleapis.com/css2?family=PT+Sans+Narrow:wght@400;700&display=swap">
<style>
  :root {
    --page: #ffffff;
    --card-top: #1470b2;
    --card-mid: #1c4f90;
    --card-bottom: #1e1a50;
    --ink: #ffffff;
    --rule: rgba(255, 255, 255, 0.55);
    --glow: rgba(170, 190, 255, 0.55);
    --device-dark: #101216;
    --device-edge: #8c9097;
    --thumb-a: #8fa6c4;
    --thumb-b: #3f5577;
  }
  * { margin: 0; padding: 0; box-sizing: border-box; }
  html, body {
    width: 1200px;
    height: 1200px;
    overflow: hidden;
    background: var(--page);
    font-family: "PT Sans Narrow", "Arial Narrow", sans-serif;
    color: var(--ink);
  }
  .canvas { position: relative; width: 1200px; height: 1200px; }

  .card {
    position: absolute;
    top: 378px;
    width: 284px;
    height: 486px;
    background: linear-gradient(180deg, var(--card-top) 0%, var(--card-mid) 40%, var(--card-bottom) 100%);
    overflow: hidden;
  }
  .card--front { left: 198px; }
  .card--back { left: 524px; }

  .hanger-hole { position: absolute; left: 100px; top: 34px; width: 94px; height: 32px; }

  .device-glow {
    position: absolute;
    border-radius: 50%;
    background: radial-gradient(ellipse at center, var(--glow) 0%, rgba(120, 140, 230, 0.18) 45%, rgba(0,0,0,0) 70%);
  }
  .device {
    position: absolute;
    border-radius: 10px;
    border: 2px solid var(--device-edge);
    background: linear-gradient(160deg, #2b2f38 0%, var(--device-dark) 55%, #1b2a44 100%);
  }

  .brand-name {
    position: absolute;
    width: 100%;
    text-align: center;
    font-weight: 700;
    line-height: 1;
    letter-spacing: 2px;
    text-transform: uppercase;
  }
  .brand-tag {
    position: absolute;
    width: 100%;
    text-align: center;
    font-weight: 400;
    text-transform: uppercase;
  }

  .tagline {
    position: absolute;
    border-top: 1px solid var(--rule);
    border-bottom: 1px solid var(--rule);
    text-align: center;
    font-size: 11.5px;
    letter-spacing: 1px;
    text-transform: uppercase;
    line-height: 21px;
  }

  /* front */
  .card--front .device-glow { left: 70px; top: 100px; width: 150px; height: 180px; }
  .card--front .device { left: 110px; top: 125px; width: 67px; height: 128px; }
  .card--front .brand-name { top: 268px; font-size: 72px; }
  .card--front .brand-tag { top: 340px; font-size: 16px; letter-spacing: 9px; padding-left: 9px; }
  .card--front .tagline { left: 38px; top: 366px; width: 213px; }

  /* back */
  .card--back .brand-name { top: 82px; font-size: 52px; }
  .card--back .brand-tag { top: 133px; font-size: 11px; letter-spacing: 6px; padding-left: 6px; }

  .feature-list { position: absolute; left: 23px; top: 167px; width: 250px; list-style: none; }
  .feature {
    position: absolute;
    display: flex;
    align-items: flex-start;
    gap: 7px;
    width: 125px;
    font-size: 12px;
    line-height: 12px;
    letter-spacing: 0.3px;
  }
  .feature-thumb {
    flex: none;
    width: 31px;
    height: 31px;
    background: linear-gradient(135deg, var(--thumb-a) 0%, var(--thumb-b) 100%);
    border: 1px solid rgba(255,255,255,0.6);
  }
  .feature-label { padding-top: 2px; }

  .card--back .device-glow { left: 80px; top: 318px; width: 120px; height: 140px; }
  .card--back .device { left: 110px; top: 338px; width: 53px; height: 102px; border-radius: 8px; }
  .card--back .tagline { left: 32px; top: 453px; width: 230px; }
</style>
</head>
<body>
<main class="canvas">

  <section class="card card--front" aria-label="Pack front">
    <svg class="hanger-hole" viewBox="0 0 94 32" aria-hidden="true">
      <circle cx="45" cy="11" r="10" fill="#ffffff"/>
      <rect x="0" y="11" width="94" height="21" rx="10.5" fill="#ffffff"/>
    </svg>
    <div class="device-glow"></div>
    <div class="device" role="img" aria-label="Illustration of a smartphone with a protected screen"></div>
    <h1 class="brand-name">vela</h1>
    <p class="brand-tag">Guardwrap</p>
    <p class="tagline">Advanced Impact Protection Shield</p>
  </section>

  <section class="card card--back" aria-label="Pack back">
    <svg class="hanger-hole" viewBox="0 0 94 32" aria-hidden="true">
      <circle cx="45" cy="11" r="10" fill="#ffffff"/>
      <rect x="0" y="11" width="94" height="21" rx="10.5" fill="#ffffff"/>
    </svg>
    <h2 class="brand-name">vela</h2>
    <p class="brand-tag">Guardwrap</p>

    <ul class="feature-list">
      <li class="feature" style="left:0;top:0"><span class="feature-thumb" role="img" aria-label="Photo of fingers applying the film"></span><span class="feature-label">Easy and Fast Application</span></li>
      <li class="feature" style="left:129px;top:0"><span class="feature-thumb" role="img" aria-label="Photo of a phone held in hand"></span><span class="feature-label">Anti Fingerprint</span></li>
      <li class="feature" style="left:0;top:39px"><span class="feature-thumb" role="img" aria-label="Photo of a stylus on a screen"></span><span class="feature-label">Compatible With Stylus</span></li>
      <li class="feature" style="left:129px;top:39px"><span class="feature-thumb" role="img" aria-label="Photo of a smooth applied screen"></span><span class="feature-label">No Air Bubble</span></li>
      <li class="feature" style="left:0;top:78px"><span class="feature-thumb" role="img" aria-label="Photo of a touchscreen in use"></span><span class="feature-label">Guaranteed Glue Free</span></li>
      <li class="feature" style="left:129px;top:78px"><span class="feature-thumb" role="img" aria-label="Photo of a clean protected screen"></span><span class="feature-label">Anti-Bacterial</span></li>
      <li class="feature" style="left:0;top:117px"><span class="feature-thumb" role="img" aria-label="Photo of a crystal clear display"></span><span class="feature-label">Perfect Crystal Clear</span></li>
      <li class="feature" style="left:129px;top:117px"><span class="feature-thumb" role="img" aria-label="Photo of a scratch resistant surface"></span><span class="feature-label">Anti Scratch</span></li>
    </ul>

    <div class="device-glow"></div>
    <div class="device" role="img" aria-label="Illustration of a smartphone with a protected screen"></div>
    <p class="tagline">Advanced Impact Protection Shield</p>
  </section>

</main>
</body>
</html>
```